Neudesign von Visitenkarten und Briefpapier für Eventmanager
Zielgruppe
Als Eventmanager bin ich seit mehr als 15 Jahren in verschiedenen Tätigkeitsfeldern und Veranstaltungsbereichen tätig.
Wechselnde Auftraggeber, Arbeitsfelder und Themen prägen meinen beruflichen Alltag.
Die Bandbreite der Tätigkeiten reicht von Organisation und Durchführung über Konzeption und Planung bis zu Management und Beratung.
Schwerpunkt und Gemeinsamkeit ist eine planerische Tätigkeit mit Umsetzung vor Ort.
Das Wort Produktionsbüro spielt in meinen Tätigkeiten immer eine große Rolle. Produktionsbüros sind die zentrale Schaltstelle bei Veranstaltungen.
Die Domain www.taktwerkstatt.de ist meine. (es gibt keinen Internetauftritt)
Bereiche: Corporate Events, Entertainment und Musik-Tourneen, Ausstellungen
international tätig
Auftraggeber sind sowohl Endkunden als auch Agenturen aus den verschiedenen Bereichen. (Eventagenturen, Tournee- und Konzertveranstalter, internationale Ausstellungsgesellschaften)
Aufgabenstellung
Entwicklung einer Wort-/Bildmarke
Stichworte: sachlich, schnörkellos, klar, nicht verspielt, zeitlos
Gestaltung von Visitenkarten und Briefpapier
Das Design muß sich ändern lassen (z.B. Umzug) und rein digital verwendbar sein – kein Druck von Briefpapier, sondern Korrespondenz lediglich digital aus MS Word/Word für MAC.
Mögliche Ansätze:
„Dornhagen“ als Personen- und Markennamen hervorheben
„stage bureau“ als überspannenden Tätigkeitsbegriff und -namen hervorheben
Das Design sollte s/w (Grautöne) oder farblich dezent sein (1 Farbe + Grau).
Im Anhang mein derzeitiges Briefpapier und die Visitenkarte. Alle diese Information sollen auch zukünftig Platz finden.

```html
<!DOCTYPE html>
<html lang="de">
<head>
<meta charset="utf-8">
<title>Dornhagen Stage Bureau – Visitenkarte</title>
<link rel="stylesheet" href="https://fonts.googleapis.com/css2?family=Arimo:wght@400;700&display=swap">
<style>
  :root {
    --brand-red: #cc0a1c;
    --ink-grey: #6b6b6b;
    --paper: #ffffff;
    --backdrop: #dcd8d0;
  }
  * { margin: 0; padding: 0; box-sizing: border-box; }
  html, body {
    width: 1045px;
    height: 1200px;
    overflow: hidden;
    background: var(--backdrop);
    font-family: "Arimo", Arial, sans-serif;
  }
  .card {
    position: absolute;
    background: var(--paper);
    overflow: hidden;
  }
  .card--front { left: 170px; top: 112px; width: 728px; height: 428px; }
  .card--back  { left: 168px; top: 617px; width: 736px; height: 432px; }

  .wordmark {
    position: absolute;
    left: 145px;
    bottom: 118px;
    color: var(--brand-red);
    font-weight: 700;
    font-size: 46px;
    line-height: 1;
    letter-spacing: -0.5px;
    white-space: nowrap;
  }
  .band {
    position: absolute;
    left: 0;
    right: 0;
    bottom: 0;
    background: var(--brand-red);
    color: var(--paper);
  }
  .card--front .band { height: 113px; padding: 18px 0 0 34px; }
  .services {
    list-style: none;
    font-size: 24px;
    letter-spacing: 1.6px;
    line-height: 36px;
    white-space: nowrap;
  }
  .card--back .band {
    height: 114px;
    display: flex;
    align-items: center;
    justify-content: center;
  }
  .holder-name {
    font-size: 35px;
    font-weight: 400;
    letter-spacing: 0.5px;
  }
  .contact {
    position: absolute;
    left: 147px;
    top: 108px;
    color: var(--ink-grey);
    font-size: 27px;
    line-height: 39px;
    font-style: normal;
  }
  .contact p + p { margin-top: 26px; }
</style>
</head>
<body>
  <section class="card card--front">
    <div class="wordmark">dornhagen stage bureau</div>
    <div class="band">
      <ul class="services">
        <li>corporate events · konzeption · organisation</li>
        <li>management · entertainment · ausstellungen</li>
      </ul>
    </div>
  </section>

  <section class="card card--back">
    <address class="contact">
      <p>ahornweg 4 c<br>51789 lindlar</p>
      <p>dornhagen@taktwerkstatt.de<br>0171.58302716</p>
    </address>
    <div class="band">
      <h1 class="holder-name">JONAS DORNHAGEN</h1>
    </div>
  </section>
</body>
</html>
```